We are full service plumbing contractors that are capable of performing all of your plumbing need...

A clean, crisp website that conveys we can handle any plumbing from drain cleaning, repairs, to new construction. But emphasis on Leak detection, under-slab and underground water service leaks, repairs, and reroutes. Leak detection by acoustical, Thermal, or tracer gas , methods.Also emphasize advanced drain cleaning technologies and equipment. Don't just poke ahole in the drain blockage, Clean the pipe, with our High pressure hydrojetters, or Chain knocker drain cables that expand to the width of the pipe being cleaned.

Number of Pages Required

5+ page

Font styles to use
Sans Serif

Requirements
Should not have
• Canned photos

```html
<!DOCTYPE html>
<html lang="en">
<head>
<meta charset="utf-8">
<title>Flowcrest Plumbing</title>
<link href="https://fonts.googleapis.com/css2?family=Roboto+Condensed:wght@400;700&family=Open+Sans:wght@400;600&display=swap" rel="stylesheet">
<style>
:root{
  --navy:#173474;
  --red:#e8202a;
  --ink:#1c1c1c;
  --muted:#444;
  --paper:#ececec;
  --white:#fff;
  --footer:#0b0c22;
  --footer-line:#2a2c48;
  --head:'Roboto Condensed',Arial,sans-serif;
  --body:'Open Sans',Arial,sans-serif;
}
*{box-sizing:border-box;margin:0;padding:0}
html,body{width:1200px;height:2778px;overflow:hidden}
body{position:relative;background:var(--white);font-family:var(--body);color:var(--ink)}
.abs{position:absolute}
.ph{position:absolute}

/* top bar */
.topbar{left:0;top:0;width:1200px;height:83px;background:var(--navy)}
.brand{left:159px;top:14px;font-family:var(--head);font-weight:700;font-size:24px;color:var(--red);letter-spacing:.5px;display:flex;align-items:center;gap:8px}
.brand-dot{width:14px;height:14px;border-radius:50%;background:var(--red)}
.contact-top{top:18px;display:flex;align-items:center;gap:10px;color:#fff;font-family:var(--head)}
.contact-top small{display:block;font-size:11px;font-weight:700;letter-spacing:.5px}
.contact-top b{display:block;font-size:17px}
.nav{left:159px;top:67px;width:730px;height:37px;background:#fff;display:flex;align-items:center;gap:24px;padding-left:24px;font-family:var(--head);font-size:11px;font-weight:700;color:#222;letter-spacing:.5px;z-index:10;box-shadow:0 2px 4px rgba(0,0,0,.12)}
.nav .on{color:var(--red)}
.nav-btn{left:889px;top:63px;width:152px;height:41px;background:var(--red);color:#fff;font-family:var(--head);font-size:11px;font-weight:700;display:flex;align-items:center;justify-content:center;gap:8px;z-index:10}

/* hero */
.hero-photo{left:0;top:83px;width:1200px;height:602px;background:linear-gradient(100deg,#7d8a99 0%,#a8b2bd 35%,#c9ccd0 55%,#6a7fa8 80%,#3a5a96 100%)}
.hero-curve{left:0;top:560px}
.hero-title{left:159px;top:205px;font-family:var(--head);font-weight:700;font-size:48px;line-height:46px;color:#fff;letter-spacing:1px}
.hero-list{left:159px;top:322px;list-style:none;color:#fff;font-family:var(--head);font-size:11px;letter-spacing:.5px}
.hero-list li{display:flex;align-items:center;gap:12px;height:26px}
.hero-list i{width:18px;height:18px;border-radius:50%;background:#fff;display:inline-block;position:relative}
.hero-list i::after{content:"";position:absolute;left:6px;top:4px;width:5px;height:8px;border:solid var(--red);border-width:0 2px 2px 0;transform:rotate(40deg)}
.hero-btn{left:159px;top:449px;width:176px;height:37px;background:var(--red);color:#fff;font-family:var(--head);font-size:11px;font-weight:700;display:flex;align-items:center;justify-content:center;gap:8px}
.slide-arrow{width:41px;height:41px;background:rgba(60,60,60,.55);display:flex;align-items:center;justify-content:center}

/* about */
.about{left:0;top:685px;width:1200px;height:339px;background:var(--paper)}
.thumb{border-radius:2px}
.sec-title{font-family:var(--head);font-weight:700;font-size:17px;letter-spacing:.5px;color:var(--ink);display:flex;align-items:center;gap:8px}
.sec-title span{color:var(--red)}
.sec-title::after{content:"";width:34px;height:2px;background:var(--red)}
.about-text{left:482px;top:784px;width:560px;font-size:10px;line-height:21px;color:#333}
.about-list{left:482px;top:880px;list-style:none;font-size:10px;color:#333}
.about-list li{height:22.5px;display:flex;align-items:center;gap:14px}
.about-list li::before{content:"";width:8px;height:8px;border-radius:50%;background:#222}

/* services */
.service{width:267px;height:130px;background:#fff;border:1px solid #e4e4e4;box-shadow:0 2px 6px rgba(0,0,0,.05);padding:22px 14px 0 14px;display:flex;gap:14px}
.service svg{flex:0 0 76px}
.service h3{font-family:var(--body);font-size:11px;font-weight:600;color:var(--red);margin-bottom:6px}
.service p{font-size:9.5px;line-height:13px;color:#222}

/* testimonial */
.testi{left:0;top:1935px;width:1200px;height:395px;background:var(--paper)}
.quote-text{left:230px;top:2180px;width:740px;text-align:center;font-size:10px;line-height:21px;color:#333}
.quote-name{left:0;top:2258px;width:1200px;text-align:center;font-size:10px;font-style:italic;color:var(--red)}
.round-arrow{width:22px;height:22px;border-radius:50%;background:#9a9a9a;display:flex;align-items:center;justify-content:center}

/* contact strip */
.strip{left:0;top:2370px;width:1200px;height:121px;background:#e6e6e6}
.cbox{top:2396px;width:282px;height:69px;border:1px solid var(--red);background:#fff;display:flex}
.cbox .ic{width:66px;background:var(--red);display:flex;align-items:center;justify-content:center}
.cbox .tx{padding:12px 0 0 14px;font-size:10px;line-height:18px;color:#222}
.cbox .tx b{display:block;font-family:var(--head);color:var(--red);font-size:10px;letter-spacing:.5px}

/* footer */
.footer{left:0;top:2491px;width:1200px;height:287px;background:var(--footer)}
.f-brand{left:159px;top:2556px;font-family:var(--head);font-weight:700;font-size:26px;color:var(--red);display:flex;align-items:center;gap:8px}
.f-about{left:159px;top:2628px;width:200px;font-size:9.5px;line-height:15px;color:#c8c8d4}
.f-col{top:2520px;width:205px}
.f-col h4{font-family:var(--head);font-size:10px;font-weight:700;color:var(--red);letter-spacing:.5px;margin-bottom:16px}
.f-col ul{list-style:none}
.f-col li{height:31px;border-bottom:1px solid var(--footer-line);font-size:9.5px;color:#c8c8d4;display:flex;align-items:center;gap:16px;padding-left:2px}
.f-col li::before{content:"›";color:#aaa}
.f-col p{font-size:9.5px;line-height:15px;color:#c8c8d4}
.f-input{width:208px;height:34px;border:1px solid #666;margin-top:14px;font-size:9.5px;color:#ccc;padding:11px 8px}
.f-submit{width:208px;height:34px;background:var(--red);margin-top:10px}
.copy{left:0;top:2750px;width:1200px;text-align:center;font-size:9.5px;color:#777}
</style>
</head>
<body>

<!-- header -->
<div class="abs topbar"></div>
<div class="abs brand"><span class="brand-dot"></span>Flowcrest</div>
<div class="abs contact-top" style="left:713px">
  <svg width="26" height="18" viewBox="0 0 26 18"><rect x="1" y="1" width="24" height="16" fill="#fff"/><path d="M1 1l12 9 12-9" fill="none" stroke="#173474" stroke-width="2"/></svg>
  <div><small>REACH US AT</small><b>INFO@DEMO.COM</b></div>
</div>
<div class="abs contact-top" style="left:905px">
  <svg width="26" height="26" viewBox="0 0 26 26"><circle cx="13" cy="13" r="12" fill="none" stroke="#fff" stroke-width="2"/><text x="13" y="17" font-size="10" font-family="Arial" font-weight="700" fill="#fff" text-anchor="middle">24</text></svg>
  <div><small>CALL US AT</small><b>999-999-9999</b></div>
</div>

<!-- hero -->
<div class="ph hero-photo" role="img" aria-label="Plumber tightening a pipe fitting under a bathroom sink"></div>
<svg class="abs hero-curve" width="1200" height="125" viewBox="0 0 1200 125">
  <path d="M0 30 Q560 190 1200 80 L1200 125 L0 125Z" fill="#ececec"/>
  <path d="M760 108 Q1000 100 1200 80" fill="none" stroke="#173474" stroke-width="4"/>
</svg>

<nav class="abs nav"><span class="on">HOME</span><span>ABOUT US</span><span>SERVICES</span><span>BLOG</span><span>CONTACT US</span></nav>
<div class="abs nav-btn">
  <svg width="14" height="14" viewBox="0 0 14 14"><circle cx="7" cy="7" r="6" fill="#fff"/><path d="M4.5 5.5l2 2 3-3" fill="none" stroke="#e8202a" stroke-width="1.5"/></svg>BOOK AN APPOINTMENT
</div>

<h1 class="abs hero-title">PLUMBING SERVICE<br>DRAIN CLEANING</h1>
<ul class="abs hero-list">
  <li><i></i>LOREM IPSUM DOLOR SIT AMET, CONSECTETUR ADIPISCING ELIT.</li>
  <li><i></i>NAM NON NISL ET EX VARIUS CURSUS EGET UT ELIT.</li>
  <li><i></i>PELLENTESQUE AUCTOR DOLOR EGET ALIQUET RUTRUM.</li>
  <li><i></i>IN A TORTOR AT LEOS EUISMOD EUISMOD.</li>
</ul>
<div class="abs hero-btn">BOOK AN APPOINTMENT
  <svg width="12" height="12" viewBox="0 0 12 12"><circle cx="6" cy="6" r="5.5" fill="#fff"/><path d="M5 3.5l2.5 2.5L5 8.5" fill="none" stroke="#e8202a" stroke-width="1.5"/></svg>
</div>
<div class="abs slide-arrow" style="left:18px;top:326px"><svg width="10" height="12"><path d="M8 1L2 6l6 5" fill="#fff"/></svg></div>
<div class="abs slide-arrow" style="left:1141px;top:326px"><svg width="10" height="12"><path d="M2 1l6 5-6 5" fill="#fff"/></svg></div>

<!-- about -->
<div class="abs about"></div>
<div class="ph thumb" style="left:159px;top:728px;width:132px;height:102px;background:linear-gradient(135deg,#4b5a3a,#3a7fd0)" role="img" aria-label="Gloved hand holding soil from a dug leak site"></div>
<div class="ph thumb" style="left:317px;top:752px;width:131px;height:102px;background:linear-gradient(135deg,#6b5a42,#3b3228)" role="img" aria-label="Exposed pipe in a trench"></div>
<div class="ph thumb" style="left:159px;top:857px;width:132px;height:102px;background:linear-gradient(135deg,#5a6b3a,#4a3b2a)" role="img" aria-label="Excavated water line with fittings"></div>
<div class="ph thumb" style="left:317px;top:882px;width:131px;height:101px;background:linear-gradient(135deg,#7a7a7a,#3a3a3a)" role="img" aria-label="Drain cleaning machine on a workshop floor"></div>
<h2 class="abs sec-title" style="left:482px;top:742px">ABOUT <span>FLOWCREST</span></h2>
<p class="abs about-text">Lorem ipsum dolor sit amet, consectetur adipiscing elit, sed do eiusmod tempor incididunt ut labore et dolore magna aliqua. Ut enim ad minim veniam, quis nostrud exercitation ullamco laboris nisi ut aliquip ex ea commodo consequat. Duis aute irure dolor in reprehenderit in voluptate velit esse cillum dolore eu fugiat nulla pariatur. Excepteur sint occaecat cupidatat non proident, sunt in culpa qui officia deserunt mollit anim id est laborum.</p>
<ul class="abs about-list">
  <li>Proin fermentum nisi vitae consequat congue.</li>
  <li>Etiam pretium nisi tincidunt augue auctor, ac efficitur leo egestas.</li>
  <li>Nulla volutpat turpis vitae venenatis euismod.</li>
  <li>In et nisi et nisl efficitur dapibus.</li>
  <li>Sed at tortor sodales, lacinia libero vitae, mattis tellus.</li>
</ul>

<!-- services -->
<div class="ph" style="left:148px;top:1068px;width:282px;height:423px;background:linear-gradient(180deg,#d9c2a8 0%,#2f3f66 35%,#243356 100%);border-radius:120px 120px 0 0" role="img" aria-label="Smiling plumber in work shirt holding a red pipe wrench"></div>
<div class="abs" style="left:30px;top:1488px;width:480px;height:12px;background:radial-gradient(ellipse at center,rgba(0,0,0,.18),transparent 70%)"></div>
<h2 class="abs sec-title" style="left:482px;top:1109px">OUR <span>SERVICES</span></h2>

<div class="abs service" style="left:483px;top:1161px">
  <svg width="76" height="76" viewBox="0 0 76 76" fill="none" stroke="#111" stroke-width="3"><path d="M14 20l18 18M10 24l8-8 6 6-8 8zM38 40l22 22 6-6-22-22"/><circle cx="52" cy="22" r="10"/><path d="M46 16l6 6"/></svg>
  <div><h3>Plumbing Service</h3><p>Lorem ipsum dolor sit amet, consectetur adipiscing elit. Aenean dui sapien, aliquam vel magna vel, venenatis sodales lorem.</p></div>
</div>
<div class="abs service" style="left:772px;top:1161px">
  <svg width="76" height="76" viewBox="0 0 76 76" fill="none" stroke="#111" stroke-width="3"><path d="M14 66V30a14 14 0 0 1 28 0v18a10 10 0 0 0 20 0V14"/><path d="M8 66h14M56 14h14"/></svg>
  <div><h3>Drain Cleaning</h3><p>Lorem ipsum dolor sit amet, consectetur adipiscing elit. Aenean dui sapien, aliquam vel magna vel, venenatis sodales lorem.</p></div>
</div>
<div class="abs service" style="left:483px;top:1313px">
  <svg width="76" height="76" viewBox="0 0 76 76" fill="none" stroke="#111" stroke-width="3"><path d="M20 10v24h36V10M30 10v12M46 10v12"/><path d="M38 34v12a10 10 0 0 1-10 10H14v12"/><path d="M8 68h14"/></svg>
  <div><h3>New construction</h3><p>Lorem ipsum dolor sit amet, consectetur adipiscing elit. Aenean dui sapien, aliquam vel magna vel, venenatis sodales lorem.</p></div>
</div>
<div class="abs service" style="left:772px;top:1313px">
  <svg width="76" height="76" viewBox="0 0 76 76" fill="none" stroke="#111" stroke-width="3"><path d="M8 28h30v12H8zM38 24h10v20H38M48 30h20v8H48M28 28V16h10v12"/><path d="M20 50c-4 6-4 10 0 10s4-4 0-10z" fill="#111"/></svg>
  <div><h3>Leak detection</h3><p>Lorem ipsum dolor sit amet, consectetur adipiscing elit. Aenean dui sapien, aliquam vel magna vel, venenatis sodales lorem.</p></div>
</div>

<!-- latest work -->
<h2 class="abs sec-title" style="left:159px;top:1535px">OUR <span>LATEST WORK</span></h2>
<div class="ph" style="left:159px;top:1582px;width:206px;height:146px;background:linear-gradient(135deg,#5a4a38,#2f6fbf 55%,#3a2e22)" role="img" aria-label="Blue water pipe exposed in soil"></div>
<div class="abs" style="left:383px;top:1582px;width:206px;height:146px;background:var(--red)"></div>
<svg class="abs" style="left:464px;top:1633px" width="44" height="44" viewBox="0 0 44 44"><circle cx="22" cy="22" r="21" fill="#fff"/><path d="M22 15v14M15 22h14" stroke="#e8202a" stroke-width="3"/></svg>
<div class="ph" style="left:609px;top:1582px;width:206px;height:146px;background:linear-gradient(135deg,#6b5a40,#8a7048)" role="img" aria-label="Brass valve on a buried line"></div>
<div class="ph" style="left:833px;top:1582px;width:206px;height:146px;background:linear-gradient(135deg,#4a5a3a,#3a80d0 60%,#4a3a2a)" role="img" aria-label="Gloved hand over a dug hole"></div>
<div class="ph" style="left:159px;top:1746px;width:206px;height:147px;background:linear-gradient(135deg,#7a6040,#4a3826)" role="img" aria-label="Pipe risers in a dirt trench"></div>
<div class="ph" style="left:383px;top:1746px;width:206px;height:147px;background:linear-gradient(135deg,#9a9a9a,#3a3a3a)" role="img" aria-label="Wheeled drain machine"></div>
<div class="ph" style="left:609px;top:1746px;width:206px;height:147px;background:linear-gradient(135deg,#3a2a22,#7a5a3a)" role="img" aria-label="Copper line repair in the ground"></div>
<div class="ph" style="left:833px;top:1746px;width:206px;height:147px;background:linear-gradient(135deg,#4a5a34,#7a4a2a 60%,#d8a030)" role="img" aria-label="Excavated leak with hose and tools"></div>

<!-- testimonial -->
<div class="abs testi"></div>
<h2 class="abs sec-title" style="left:159px;top:1964px">CLIENT <span>SPEAK</span></h2>
<svg class="abs" style="left:562px;top:2016px" width="40" height="32" viewBox="0 0 40 32"><path d="M2 30V16C2 8 6 3 14 1l2 4c-5 2-7 5-7 9h7v16zM22 30V16c0-8 4-13 12-15l2 4c-5 2-7 5-7 9h7v16z" fill="#d4d4d4"/></svg>
<div class="ph" style="left:541px;top:2085px;width:82px;height:82px;border-radius:50%;background:linear-gradient(180deg,#c9c9c9,#3a3a3a);border:3px solid #fff" role="img" aria-label="Client portrait"></div>
<p class="abs quote-text">Mauris eget odio faucibus, aliquet tellus sed, sagittis orci. Praesent molestie eros ac pellentesque volutpat. Interdum et malesuada fames ac ante ipsum primis in faucibus. Praesent porta sapien libero, ut sagittis neque vestibulum non. Curabitur laoreet elit eu placerat ornare. Vestibulum semper hendrerit. Cras rutrum massa nisl, vel fermentum nulla lacinia iaculis. Nulla fermentum fringilla tortor ut posuere. Nunc id suscipit quam.</p>
<p class="abs quote-name">Lorem ipsum dolor</p>
<div class="abs round-arrow" style="left:158px;top:2119px"><svg width="8" height="10"><path d="M7 1L1 5l6 4" fill="#fff"/></svg></div>
<div class="abs round-arrow" style="left:1017px;top:2119px"><svg width="8" height="10"><path d="M1 1l6 4-6 4" fill="#fff"/></svg></div>

<!-- contact strip -->
<div class="abs strip"></div>
<div class="abs cbox" style="left:159px">
  <div class="ic"><svg width="18" height="24" viewBox="0 0 18 24"><path d="M9 1a8 8 0 0 0-8 8c0 6 8 14 8 14s8-8 8-14a8 8 0 0 0-8-8z" fill="#fff"/><circle cx="9" cy="9" r="3" fill="#e8202a"/></svg></div>
  <div class="tx"><b>VISIT US:</b>Contrary to popular belief,<br>Lorem Ipsum is not simply</div>
</div>
<div class="abs cbox" style="left:459px">
  <div class="ic"><svg width="24" height="18" viewBox="0 0 24 18"><rect width="24" height="18" fill="#fff"/><path d="M0 0l12 9 12-9" fill="none" stroke="#e8202a" stroke-width="2"/></svg></div>
  <div class="tx"><b>MAIL US AT:</b>info@demo.com</div>
</div>
<div class="abs cbox" style="left:759px">
  <div class="ic"><svg width="22" height="22" viewBox="0 0 22 22"><path d="M5 2l4 4-2 3c1 3 3 5 6 6l3-2 4 4-3 3C9 20 2 13 2 5z" fill="#fff"/></svg></div>
  <div class="tx"><b>CALL US AT:</b>999-999-9999<br>999-999-9999</div>
</div>

<!-- footer -->
<div class="abs footer"></div>
<div class="abs f-brand"><span class="brand-dot"></span>Flowcrest</div>
<p class="abs f-about">Lorem ipsum dolor sit amet, consectetur adipiscing elit. Aliquam auctor odio molestie, vehicula massa faucibus, tincidunt odio. Phasellus ornare non ligula in rutrum. In hac habitasse platea dictumst.</p>
<div class="abs f-col" style="left:383px"><h4>QUICK LINKS</h4>
  <ul><li>Home</li><li>About us</li><li>Services</li><li>Blog</li><li>Contact Us</li></ul></div>
<div class="abs f-col" style="left:609px"><h4>SERVICES</h4>
  <ul><li>Plumbing Service</li><li>Drain Cleaning</li><li>New construction</li><li>Leak detection</li><li>Faucet Repairs</li></ul></div>
<div class="abs f-col" style="left:833px"><h4>SUBSCRIBE NOW!</h4>
  <p>Lorem ipsum dolor sit amet, consectetur adipiscing elit. Aliquam auctor odio molestie, vehicula massa faucibus, tincidunt odio.</p>
  <div class="f-input">Enter your Email</div>
  <div class="f-submit"></div></div>
<p class="abs copy">Copyright © Flowcrest Plumbing 2019 All rights reserved.</p>

</body>
</html>
```